Trolvex.ai

Australian based application building technology company. website (trolvex.ai) servicing the retail and shopping industries, IoT
Similar services to https://quarnel.com/.
Logo attached

Target Market(s)

Technology Retail

Industry/Entity Type

It Company

Number of Pages Required

2 page

Font styles to use
Other font styles liked:
• We will supply

Colors
ec1f27

Requirements
Must have
• responsive, extra small, small, medium, large, wide
Nice to have
• Modern, sophisticated, current and ON trende
Should not have
• Over saturation, keep it simple, smart and easy navigation

```html
<!DOCTYPE html>
<html lang="en">
<head>
<meta charset="utf-8">
<title>Trolvex – Application Building Technology</title>
<link rel="stylesheet" href="https://fonts.googleapis.com/css2?family=Montserrat:wght@400;600;700&family=Open+Sans:wght@400;600&display=swap">
<style>
:root{
  --red:#ec1f27;
  --red-dark:#b3141b;
  --ink:#1f1f1f;
  --text:#555;
  --grey-bg:#e9e9e9;
  --line:#d8d8d8;
  --white:#fff;
}
*{box-sizing:border-box;margin:0;padding:0}
html,body{width:1200px;height:4317px;overflow:hidden}
body{position:relative;background:var(--white);font-family:"Open Sans",Arial,sans-serif;color:var(--text)}
.section{position:absolute;left:0;width:1200px}
.abs{position:absolute}
.btn{position:absolute;display:flex;align-items:center;justify-content:center;background:var(--red);color:var(--white);font:600 11px "Montserrat",sans-serif;letter-spacing:.5px;text-transform:uppercase}
.btn-outline{background:var(--white);color:var(--red);border:2px solid var(--red)}
.section-title{position:absolute;left:0;width:1200px;text-align:center;color:var(--red);font:700 27px "Montserrat",sans-serif;letter-spacing:1px}
.title-rule{position:absolute;left:560px;width:80px;height:3px;background:var(--line)}
.brand{display:flex;align-items:center;gap:10px;color:var(--red);font:700 30px "Montserrat",sans-serif}
.brand-mark{width:34px;height:34px;border-radius:50%;background:var(--red)}

/* header */
.site-header{top:0;height:95px}
.nav a{position:absolute;top:36px;height:26px;display:flex;align-items:center;justify-content:center;font:600 11px "Montserrat",sans-serif;color:var(--ink);text-transform:uppercase;text-decoration:none}
.nav .active{background:var(--red);color:var(--white)}

/* hero */
.hero{top:95px;height:578px;background:linear-gradient(100deg,#6d6a5a 0%,#a7a28a 30%,#8c8a78 55%,#c9c3ae 75%,#7c7766 100%)}
.hero-title{left:178px;top:180px;width:490px;height:130px;background:rgba(30,30,30,.82);color:var(--white);font:700 45px/1.15 "Montserrat",sans-serif;padding:14px 20px}
.hero-dots{left:540px;top:512px;display:flex;gap:16px}
.hero-dots span{width:10px;height:10px;border-radius:50%;background:rgba(255,255,255,.6)}
.hero-dots span:first-child{background:var(--white)}

/* features */
.features{top:673px;height:642px}
.feature-art{left:130px;top:177px;width:418px;height:405px;background:linear-gradient(180deg,#f2f2f2,#dcdcdc)}
.feature-heading{left:607px;top:225px;width:420px;font:600 28px/1.25 "Montserrat",sans-serif;color:var(--ink)}
.feature-text{left:612px;top:322px;width:410px;font-size:12px;line-height:1.75}

/* videos */
.videos{top:1315px;height:615px;background:var(--grey-bg)}
.video-frame{left:245px;top:168px;width:710px;height:389px;background:linear-gradient(180deg,#c0141c,#a5060e);box-shadow:0 2px 8px rgba(0,0,0,.2)}
.play{left:555px;top:330px}

/* benefits */
.benefits{top:1930px;height:570px}
.benefit-card{position:absolute;top:203px;width:250px;height:287px;border:1px solid var(--line);text-align:center}
.benefit-card svg{position:absolute;left:80px;top:28px}
.benefit-card h3{position:absolute;top:152px;width:100%;font:600 18px "Montserrat",sans-serif;color:var(--ink)}
.benefit-card .btn{left:72px;top:215px;width:106px;height:33px}

/* promo */
.promo{top:2500px;height:490px;background:var(--grey-bg)}
.promo-heading{left:130px;top:100px;width:360px;font:600 30px/1.25 "Montserrat",sans-serif;color:var(--ink)}
.promo-text{left:130px;top:200px;width:370px;font-size:12px;line-height:1.75}
.promo-art{left:547px;top:70px;width:525px;height:345px;background:linear-gradient(90deg,#2a2a35,#4b4b60 50%,#2a2a35)}

/* blog */
.blog{top:2990px;height:680px}
.post{position:absolute;top:203px;width:296px;height:395px;border:1px solid var(--line);background:var(--white)}
.post-image{position:absolute;left:0;top:0;width:100%;height:192px;background:linear-gradient(135deg,#8a9aa6,#c8cfd4 60%,#6e7780)}
.post-date{position:absolute;left:24px;top:188px;background:var(--white);color:var(--ink);font:600 9px "Montserrat",sans-serif;padding:2px 6px;box-shadow:0 1px 2px rgba(0,0,0,.2)}
.post h3{position:absolute;left:24px;top:230px;width:250px;font:600 16px/1.35 "Montserrat",sans-serif;color:var(--ink)}
.post p{position:absolute;left:24px;top:292px;width:250px;font-size:12px;line-height:1.6}
.post .btn{left:24px;top:352px;width:86px;height:26px;font-size:10px}

/* newsletter */
.newsletter{top:3670px;height:305px;background:var(--red)}
.newsletter .section-title{color:var(--white);top:62px;font-size:28px}
.newsletter .title-rule{background:var(--white);top:112px}
.field{position:absolute;top:185px;height:50px;background:var(--white);padding-left:22px;display:flex;align-items:center;font-size:13px;color:#777}
.signup{position:absolute;left:772px;top:185px;width:248px;height:50px;border:2px solid var(--white);color:var(--white);display:flex;align-items:center;justify-content:center;font:700 18px "Montserrat",sans-serif;letter-spacing:1px}

/* footer */
.site-footer{top:3975px;height:342px}
.footer-col{position:absolute;top:68px}
.footer-col h4{font:700 12px "Montserrat",sans-serif;color:var(--red);margin-bottom:12px}
.footer-col li{list-style:none;font-size:12px;line-height:20px;color:#555}
.social{display:flex;gap:14px;margin-top:2px}
.social span{width:18px;height:18px;border-radius:50%;background:#9a9a9a}
.footer-rule{left:130px;top:237px;width:940px;height:1px;background:var(--line)}
.copyright{left:0;top:284px;width:1200px;text-align:center;font-size:11px;color:#555}
</style>
</head>
<body>

<header class="section site-header">
  <div class="abs brand" style="left:130px;top:28px"><span class="brand-mark"></span>TROLVEX</div>
  <nav class="nav">
    <a class="active" style="left:460px;width:73px">Home</a>
    <a style="left:558px;width:65px">About us</a>
    <a style="left:662px;width:56px">The app</a>
    <a style="left:752px;width:40px">Blog</a>
    <a style="left:826px;width:88px">Contact us</a>
    <a class="active" style="left:941px;width:127px">Request a demo</a>
  </nav>
</header>

<section class="section hero" role="img" aria-label="Hand holding a smartphone in a supermarket aisle">
  <h1 class="abs hero-title">Application Building Technology</h1>
  <div class="abs hero-dots"><span></span><span></span><span></span><span></span><span></span></div>
</section>

<section class="section features">
  <h2 class="section-title" style="top:52px">OUR FEATURES</h2>
  <div class="title-rule" style="top:105px"></div>
  <div class="abs feature-art" role="img" aria-label="Line drawing of an office tower beside a smartphone showing app icons"></div>
  <h3 class="abs feature-heading">Retail and Shopping Industries</h3>
  <p class="abs feature-text">It simply because it is pain..." What is Lorem Ipsum? Lorem Ipsum is simply dummy text of the printing and typesetting industry. Lorem Ipsum has been the industry's standard dummy text ever since the 1500s, when an unknown printer took a galley of type and scrambled it to make a type specimen book.</p>
  <a class="btn" style="left:613px;top:470px;width:132px;height:42px">Learn more</a>
</section>

<section class="section videos">
  <h2 class="section-title" style="top:52px">OUR VIDEOS</h2>
  <div class="title-rule" style="top:105px"></div>
  <div class="abs video-frame" role="img" aria-label="Video preview on red: in-store engagement, mapping, navigation and analytics"></div>
  <svg class="abs play" width="90" height="58" viewBox="0 0 90 58"><rect width="90" height="58" rx="6" fill="#fff" opacity=".9"/><path d="M36 16 L58 29 L36 42Z" fill="#222"/></svg>
</section>

<section class="section benefits">
  <h2 class="section-title" style="top:70px">WHO BENEFITS?</h2>
  <div class="title-rule" style="top:123px"></div>
  <div class="benefit-card" style="left:190px">
    <svg width="90" height="100" viewBox="0 0 90 100"><path d="M30 30 V20 a15 15 0 0 1 30 0 V30" fill="none" stroke="#222" stroke-width="5"/><rect x="8" y="30" width="74" height="62" fill="none" stroke="#222" stroke-width="6"/><path d="M32 55 a13 13 0 0 0 26 0" fill="none" stroke="#222" stroke-width="5"/></svg>
    <h3>Retail</h3>
    <a class="btn btn-outline">See more</a>
  </div>
  <div class="benefit-card" style="left:475px">
    <svg width="90" height="100" viewBox="0 0 90 100"><path d="M8 20 H82 L88 42 H2Z" fill="#222"/><path d="M2 42 h86 v8 a10 10 0 0 1 -86 0z" fill="#222"/><rect x="10" y="55" width="70" height="40" fill="#222"/><rect x="30" y="65" width="30" height="30" fill="#fff"/><path d="M20 20 L16 42 M36 20 L34 42 M54 20 L56 42 M70 20 L74 42" stroke="#fff" stroke-width="3"/></svg>
    <h3>Shopping Industries</h3>
    <a class="btn btn-outline">See more</a>
  </div>
  <div class="benefit-card" style="left:760px">
    <svg width="90" height="100" viewBox="0 0 90 100"><circle cx="45" cy="30" r="20" fill="#222"/><path d="M6 95 C8 65 22 55 45 55 C68 55 82 65 84 95Z" fill="#222"/></svg>
    <h3>IoT firms</h3>
    <a class="btn btn-outline">See more</a>
  </div>
</section>

<section class="section promo">
  <h2 class="abs promo-heading">It is a long established fact that a reader</h2>
  <p class="abs promo-text">It simply because it is pain..." What is Lorem Ipsum? Lorem Ipsum is simply dummy text of the printing and typesetting industry. Lorem Ipsum has been the industry's standard dummy text ever since the 1500s, when an unknown printer took a galley of type and scrambled.</p>
  <a class="btn" style="left:130px;top:345px;width:134px;height:42px">Learn more</a>
  <div class="abs promo-art" role="img" aria-label="Three smartphones showing chat, app icons and a music player"></div>
</section>

<section class="section blog">
  <h2 class="section-title" style="top:70px">OUR BLOG</h2>
  <div class="title-rule" style="top:123px"></div>
  <article class="post" style="left:130px">
    <div class="post-image" role="img" aria-label="Hand holding a phone"></div>
    <span class="post-date">MAY 15, 2017</span>
    <h3>Lorem Ipsum is simply dummy text of the printing.</h3>
    <p>It is a long established fact that a re ader will be distracted by the readable</p>
    <a class="btn">Read more</a>
  </article>
  <article class="post" style="left:452px">
    <div class="post-image" role="img" aria-label="Hands using a phone"></div>
    <span class="post-date">MAY 15, 2017</span>
    <h3>There are many variations of passages of Lorem Ipsum.</h3>
    <p>It is a long established fact that a re ader will be distracted by the readable</p>
    <a class="btn">Read more</a>
  </article>
  <article class="post" style="left:774px">
    <div class="post-image" role="img" aria-label="Person scrolling on a phone"></div>
    <span class="post-date">MAY 15, 2017</span>
    <h3>Sed ut perspiciatis unde omnis iste natus error</h3>
    <p>It is a long established fact that a re ader will be distracted by the readable</p>
    <a class="btn">Read more</a>
  </article>
</section>

<section class="section newsletter">
  <h2 class="section-title">NEWSLETTER SIGNUP</h2>
  <div class="title-rule"></div>
  <div class="field" style="left:248px;width:239px">Name</div>
  <div class="field" style="left:507px;width:239px">E-mail id</div>
  <div class="signup">SIGNUP</div>
</section>

<footer class="section site-footer">
  <div class="abs brand" style="left:130px;top:78px"><span class="brand-mark"></span>TROLVEX</div>
  <div class="footer-col" style="left:449px"><h4>PRODUCTS</h4><ul><li>Platform</li><li>Beacons</li><li>Browsers</li><li>QR</li><li>NFC</li></ul></div>
  <div class="footer-col" style="left:613px"><h4>MENU</h4><ul><li>Home</li><li>About us</li><li>The app</li><li>Blog</li><li>Contact us</li></ul></div>
  <div class="footer-col" style="left:757px"><h4>SUPPORT</h4><ul><li>Knowledge Base</li><li>Frequent Questions</li><li>Community Forum</li><li>Contact Us</li></ul></div>
  <div class="footer-col" style="left:938px"><h4>FOLLOW US ON</h4><div class="social"><span></span><span></span><span></span><span></span></div></div>
  <div class="abs footer-rule"></div>
  <p class="abs copyright">Copyright © 2017 All Rights Reserved</p>
</footer>

</body>
</html>
```